20 year old business card needs re-design

We need to redesign our corporate business card look. We need something that appears more modern, eye catchy but professional.

Target Market(s)

manufacturing industry

Industry/Entity Type

Manufacturer

Contact Information for Business Card

One side can have the logo. Other side can have contact information.

Font styles to use
Serif

Colors
3277b5
33b8a4
ffffff

Requirements
Must have
• Eye catchy - need to standout from the crowd. company logo cannot change. Full name, job title, phone number and email address.
Should not have
• Fax, business address is not necessary.

```html
<!DOCTYPE html>
<html lang="en">
<head>
<meta charset="utf-8">
<title>Norvatek Global – Business Card</title>
<link href="https://fonts.googleapis.com/css2?family=Tinos:ital,wght@0,400;0,700;1,400;1,700&display=swap" rel="stylesheet">
<style>
  :root {
    --brand-blue: #3277b5;
    --band-blue: #2f68b4;
    --band-dark: #1f4f94;
    --ink: #2b2b2b;
    --ink-soft: #4a4a4a;
    --paper: #ffffff;
    --paper-shade: #eceff2;
    --stage: #e4e6e9;
  }
  * { box-sizing: border-box; margin: 0; padding: 0; }
  html, body { width: 1200px; height: 780px; overflow: hidden; }
  body {
    background: var(--stage);
    font-family: "Tinos", "Times New Roman", serif;
    position: relative;
  }
  .card {
    position: absolute;
    width: 560px;
    height: 320px;
    border-radius: 16px;
    background: linear-gradient(160deg, var(--paper) 0%, var(--paper) 55%, var(--paper-shade) 100%);
    box-shadow: 0 6px 18px rgba(0,0,0,0.18);
    overflow: hidden;
  }
  .card--front { left: 40px; top: 50px; }
  .card--back { left: 600px; top: 410px; }

  .card__band {
    position: absolute;
    left: 0; right: 0; bottom: 0;
    height: 44px;
    background: linear-gradient(180deg, var(--band-blue), var(--band-dark));
    border-top: 3px solid #3a3a3a;
    color: var(--paper);
    display: flex;
    align-items: center;
    justify-content: center;
    font-size: 15px;
    letter-spacing: 0.3px;
  }
  .card--back .card__band { font-style: italic; font-weight: 700; }

  .wordmark {
    display: flex;
    align-items: center;
    gap: 8px;
    color: var(--ink);
    font-weight: 700;
    white-space: nowrap;
  }
  .wordmark__square {
    width: 12px; height: 12px;
    flex: none;
    background: var(--brand-blue);
  }
  .card--front .wordmark {
    position: absolute;
    left: 26px; top: 156px;
    width: 236px;
    font-size: 24px;
  }
  .card--back .wordmark {
    position: absolute;
    left: 0; right: 0; top: 108px;
    justify-content: center;
    gap: 10px;
    font-size: 46px;
  }
  .card--back .wordmark__square { width: 14px; height: 14px; }

  .divider {
    position: absolute;
    left: 274px; top: 40px;
    width: 2px; height: 200px;
    background: var(--brand-blue);
  }

  .contact {
    position: absolute;
    left: 294px; top: 38px;
    width: 250px;
    color: var(--ink-soft);
    font-size: 14px;
    line-height: 1.35;
  }
  .contact__name {
    color: var(--brand-blue);
    font-size: 23px;
    font-weight: 700;
    line-height: 1.1;
  }
  .contact__title { font-size: 15px; margin-bottom: 10px; color: var(--ink); }
  .contact__line { display: flex; align-items: center; gap: 7px; }
  .contact__icon { width: 16px; height: 16px; flex: none; }
  .contact__offices { margin-top: 10px; }
  .contact__cert { margin-top: 8px; color: var(--brand-blue); }
</style>
</head>
<body>

  <section class="card card--front" aria-label="Business card, contact side">
    <div class="wordmark"><span class="wordmark__square"></span>Norvatek Global</div>
    <div class="divider"></div>
    <div class="contact">
      <p class="contact__name">Daniel Reyes</p>
      <p class="contact__title">Senior Project Manager</p>
      <p class="contact__line">
        <svg class="contact__icon" viewBox="0 0 16 16" aria-hidden="true">
          <rect width="16" height="16" rx="2" fill="#3277b5"/>
          <path d="M5 3.5c.6 0 1.3 1.7 1.3 2.2 0 .6-.8.8-.8 1.3 0 .8 1.7 2.6 2.5 2.6.5 0 .7-.8 1.3-.8.5 0 2.2.7 2.2 1.3 0 1.1-1.1 2.4-2.3 2.4C6.4 12.5 3.5 9.5 3.5 6.6 3.5 5 4.3 3.5 5 3.5z" fill="#fff"/>
        </svg>
        555-014-2200 xt 118
      </p>
      <p class="contact__line">
        <svg class="contact__icon" viewBox="0 0 16 16" aria-hidden="true">
          <rect width="16" height="16" rx="2" fill="#3277b5"/>
          <rect x="3" y="4.5" width="10" height="7" fill="none" stroke="#fff" stroke-width="1.2"/>
          <path d="M3 4.8l5 4 5-4" fill="none" stroke="#fff" stroke-width="1.2"/>
        </svg>
        daniel@norvatekglobal.com
      </p>
      <p class="contact__offices">Offices &amp; Warehousing:<br>USA - Taiwan - Mexico</p>
      <p class="contact__cert">TS16949 &amp; ISO9001 Certified Facilities</p>
    </div>
    <div class="card__band">International manufacturing solutions for OEM customers in North America</div>
  </section>

  <section class="card card--back" aria-label="Business card, logo side">
    <div class="wordmark"><span class="wordmark__square"></span>Norvatek Global</div>
    <div class="card__band">NorvatekGlobal.com</div>
  </section>

</body>
</html>
```